Logo and 1 page Flyer for Meridian Fund

We need a logo and a 1 single page flyer for an Investment Fund we'll distribute worldwide. It'a Meridian Fund that will give a return also to the poorest people in the world. Details inside. We give just an idea (based on a previous flyer we had here) with the attached draft. Anyone can figure out how to make its own. NOTE: LQV is our company's logo.

Target Market(s)

Investors

Industry/Entity Type

Finance And Accounting

Logo Text

KOLB Kindred Open Bloom Fund

Font styles to use
Serif

Colors
00a990

Requirements
Must have
• A logo you choose which should be:
• - Elegant
• - Innovative
• - Crypto evoking (Company launching is a cripto company)
• - Hi tech
Nice to have
• We have sent you all materials to be able to understand:
• 1. A draft of how we would like the texts to come out. Don't use this (we're already using with other texts), ,but see the evidence of Logo, Slogan, and the 3 main characteristics. Also notice very well that is very elegant. Use a real light on color, make it as shining as you can. It must be a sort of shining green, expressing Hope, Beauty, Well being
• 2. The logo for LQV that is the company launching the project. In draft you see on low left. You can put wherever you feel right
• 3. All texts are on draft to be seen, and on word to be used. You can choose font and dimensions as you prefer
• 4. We've given you logo we have for PIRO. If you feel, you can use in the line where we talk about it or place somewhere. Not mandatory
Should not have
• Funny things; too commercial style; unprofessional aspect

```html
<!DOCTYPE html>
<html lang="en">
<head>
<meta charset="utf-8">
<title>KOLB Kindred Open Bloom Fund – Flyer</title>
<link rel="stylesheet" href="https://fonts.googleapis.com/css2?family=Bitter:wght@800&family=Open+Sans:wght@400;700;800&family=Oswald:wght@700&display=swap">
<style>
  :root {
    --teal: #00a990;
    --teal-light: #a6e0d6;
    --brand-blue: #2a4f9a;
    --orb-deep: #1a4fc4;
    --orb-light: #3f86d8;
    --paper: #ffffff;
    --backdrop: #e9eceb;
    --ink-white: #ffffff;
    --grey-name: #7a7d82;
  }
  html, body {
    margin: 0;
    padding: 0;
    width: 1200px;
    height: 1200px;
    overflow: hidden;
    background: var(--backdrop);
  }
  .canvas {
    position: relative;
    width: 1200px;
    height: 1200px;
  }
  .flyer {
    position: absolute;
    left: 172.7px;
    top: 0;
    width: 809px;
    height: 1136px;
    transform: scale(1.0563);
    transform-origin: top left;
    background: var(--paper);
    overflow: hidden;
    font-family: "Open Sans", Arial, sans-serif;
  }
  .flyer-art {
    position: absolute;
    inset: 0;
    width: 809px;
    height: 1136px;
  }
  .brand {
    position: absolute;
    left: 38px;
    top: 26px;
  }
  .brand-row {
    display: flex;
    align-items: center;
    gap: 10px;
  }
  .brand-dot {
    width: 66px;
    height: 66px;
    border-radius: 50%;
    background: var(--brand-blue);
  }
  .brand-name {
    font-weight: 800;
    font-size: 70px;
    line-height: 1;
    color: var(--brand-blue);
    letter-spacing: -1px;
  }
  .brand-tagline {
    margin-top: 12px;
    font-family: "Bitter", Georgia, serif;
    font-weight: 800;
    font-size: 29px;
    line-height: 1;
    color: var(--brand-blue);
  }
  .site {
    position: absolute;
    right: 32px;
    top: 28px;
    display: flex;
    align-items: center;
    gap: 6px;
    font-size: 19px;
    letter-spacing: 3px;
    color: #1d2b4a;
  }
  .headline {
    position: absolute;
    left: 0;
    right: 0;
    top: 400px;
    margin: 0;
    text-align: center;
    font-family: "Oswald", "Arial Narrow", sans-serif;
    font-weight: 700;
    font-size: 50px;
    line-height: 1.1;
    color: var(--ink-white);
    letter-spacing: 0.3px;
  }
  .intro {
    position: absolute;
    left: 0;
    right: 0;
    top: 461px;
    margin: 0;
    text-align: center;
    font-weight: 700;
    font-size: 21px;
    line-height: 34px;
    color: var(--ink-white);
  }
  .features {
    position: absolute;
    left: 35px;
    top: 578px;
    width: 742px;
    table-layout: fixed;
    border-collapse: collapse;
    color: var(--ink-white);
  }
  .features .col-label { width: 288px; }
  .features td {
    box-sizing: border-box;
    border: 1.5px solid var(--ink-white);
    vertical-align: top;
    height: 71px;
    padding: 0;
    overflow: hidden;
  }
  .features .feature-label {
    padding: 9px 0 0 25px;
    font-weight: 800;
    font-size: 23px;
    line-height: 28px;
  }
  .features .feature-text {
    padding: 13px 6px 0 28px;
    font-size: 17px;
    line-height: 24px;
  }
  .features .feature-text.single {
    padding-top: 16px;
  }
  .partner {
    position: absolute;
    display: flex;
    align-items: center;
    gap: 8px;
  }
  .partner-company {
    left: 112px;
    top: 1022px;
  }
  .partner-company .partner-dot {
    width: 74px;
    height: 74px;
    border-radius: 50%;
    background: var(--orb-deep);
  }
  .partner-company .partner-name {
    font-weight: 800;
    font-size: 62px;
    line-height: 1;
    color: var(--orb-deep);
  }
  .partner-system {
    left: 520px;
    top: 1030px;
  }
  .partner-system .partner-name {
    font-weight: 800;
    font-size: 50px;
    line-height: 1;
    color: var(--grey-name);
    letter-spacing: 2px;
  }
</style>
</head>
<body>
<div class="canvas">
  <div class="flyer">
    <svg class="flyer-art" viewBox="0 0 809 1136" xmlns="http://www.w3.org/2000/svg" aria-hidden="true">
      <defs>
        <linearGradient id="orbFill" x1="0" y1="0" x2="1" y2="1">
          <stop offset="0" stop-color="#3f86d8"/>
          <stop offset="0.5" stop-color="#1a4fc4"/>
          <stop offset="1" stop-color="#2d6fd0"/>
        </linearGradient>
      </defs>
      <path class="teal-band" fill="var(--teal)"
        d="M0 388 C150 360 260 310 330 250 C380 210 430 195 480 215 C560 250 620 300 700 290 C750 285 790 268 809 262
           L809 985 C700 975 620 985 560 975 C500 965 480 870 410 866 C340 862 330 1005 280 1010 C200 1015 90 960 0 930 Z"/>
      <g class="connector-lines" stroke="var(--teal-light)" stroke-width="4">
        <line x1="118" y1="330" x2="118" y2="815"/>
        <line x1="406" y1="368" x2="406" y2="870"/>
        <line x1="677" y1="300" x2="677" y2="832"/>
      </g>
      <g class="nodes" fill="var(--teal-light)">
        <circle cx="406" cy="318" r="50"/>
        <circle cx="118" cy="864" r="50"/>
        <circle cx="677" cy="882" r="50"/>
      </g>
      <g class="orbs" fill="url(#orbFill)">
        <circle cx="124" cy="248" r="83"/>
        <circle cx="671" cy="180" r="90"/>
        <circle cx="409" cy="944" r="60"/>
      </g>
    </svg>

    <div class="brand">
      <div class="brand-row">
        <span class="brand-dot"></span>
        <span class="brand-name">KOLB</span>
      </div>
      <div class="brand-tagline">Kindred Open Bloom Fund</div>
    </div>

    <div class="site">
      <svg width="18" height="18" viewBox="0 0 20 20" aria-hidden="true">
        <g fill="none" stroke="#1d2b4a" stroke-width="1.6">
          <circle cx="10" cy="10" r="8.5"/>
          <ellipse cx="10" cy="10" rx="3.8" ry="8.5"/>
          <line x1="1.5" y1="10" x2="18.5" y2="10"/>
          <line x1="3" y1="5.5" x2="17" y2="5.5"/>
          <line x1="3" y1="14.5" x2="17" y2="14.5"/>
        </g>
      </svg>
      <span>www.lqvm.io</span>
    </div>

    <h1 class="headline">RAISE THE POOR BLOOMING WITH US</h1>
    <p class="intro">With KOLB you achieve sound return on your investment.<br>And you help needy ones to obtain real help in their life.</p>

    <table class="features">
      <colgroup>
        <col class="col-label">
        <col class="col-text">
      </colgroup>
      <tr>
        <td class="feature-label">Better RETURN</td>
        <td class="feature-text">Using PIRO – Prime Intelligent Risk Optimizer. A breaktrough in moneymanagement</td>
      </tr>
      <tr>
        <td class="feature-label">For ANYONE</td>
        <td class="feature-text">For those who can invest. And for those Whohave no money to survive.</td>
      </tr>
      <tr>
        <td class="feature-label">Money and HEARTH</td>
        <td class="feature-text single">To have a return that Warmsyou and others.</td>
      </tr>
    </table>

    <div class="partner partner-company">
      <span class="partner-dot"></span>
      <span class="partner-name">LQV</span>
    </div>
    <div class="partner partner-system">
      <span class="partner-name">PIRO</span>
    </div>
  </div>
</div>
</body>
</html>
```